needing web design for aerial and satellite installation comapny

We need our website designing, it needs to be professional and look creative,
We are a aerial and satellite company called Kestrel Mend & Reach ()
I like this site design also some of the following maybe:

https://www.skywirelo.co.uk/

http://holdmoor.co.uk/

http://quillnine-guard.co.uk/portfolio/zmp-holdmoor/

The design will require coding once the design is complete, i haven't paid for this yet as i want to be sure the design is good before i commit.

The template needs to look professional and look like one of the leading companies.
The site will consist of all the features this site has https://www.skywirelo.co.uk/

I like a modern design with the latest technology.

Target Market(s)

tv aerial satellite installation

Industry/Entity Type

Satellite Tv

Number of Pages Required

3 page

Font styles to use
Sans Serif

Colors

Designer to choose colors to be used in the design.

Requirements
Must have
• eb Contest Brief We need our website designing, it needs to be professional and look creative,
• We are a aerial and satellite company called Kestrel Mend Reach ()
• I like this site design also some of the following maybe:
• https://www.skywirelo.co.uk/
• http://holdmoor.co.uk/
• http://quillnine-guard.co.uk/portfolio/zmp-holdmoor/
• The design will require coding once the design is complete, i haven't paid for this yet as i want to be sure the design is good before i commit.
• The template needs to look professional and look like one of the leading companies.
• The site will consist of all the features this site has https://www.skywirelo.co.uk/
• I like a modern design with the latest technology.
Nice to have
• http://holdmoor.co.uk/
Should not have
• poor design

```html
<!DOCTYPE html>
<html lang="en">
<head>
<meta charset="utf-8">
<title>Kestrel Reach &amp; Mend — Aerial &amp; Satellite Installers</title>
<link href="https://fonts.googleapis.com/css2?family=Open+Sans:wght@400;600;700&family=Gelasio:wght@400&display=swap" rel="stylesheet">
<style>
:root{
  --red:#e31e24;
  --ink:#1b1b1b;
  --text:#555;
  --muted:#888;
  --line:#e6e6e6;
  --dark:#1c1c1c;
  --white:#fff;
}
*{box-sizing:border-box;margin:0;padding:0}
html,body{width:1200px;height:3120px;overflow:hidden}
body{position:relative;background:var(--white);font-family:"Open Sans",Arial,sans-serif;color:var(--text)}
.abs{position:absolute}
.serif{font-family:"Gelasio",Georgia,serif;font-weight:400}

/* hero */
.hero{left:0;top:0;width:1200px;height:670px;background:linear-gradient(180deg,#eeeeec 0%,#e3e1dc 45%,#d6d2cb 100%)}
.social-top{left:162px;top:44px;display:flex;gap:14px}
.social-top span{width:14px;height:14px;border-radius:2px;background:#6b8fc4}
.social-top span:nth-child(2){background:#5aa9e6}
.social-top span:nth-child(3){background:#d9a441}
.phone-btn{left:909px;top:31px;width:130px;height:42px;background:#222;color:#fff;font-size:13px;font-weight:600;display:flex;align-items:center;justify-content:center;gap:8px}
.brand-mark{left:557px;top:168px;width:86px;height:86px;border:6px solid var(--ink)}
.brand-name{left:0;width:1200px;text-align:center;color:var(--ink);font-weight:600}
.brand-1{top:335px;font-size:32px;letter-spacing:18px}
.brand-2{top:385px;font-size:24px;letter-spacing:20px}
.hero-title{left:0;width:1200px;top:478px;text-align:center;font-size:30px;color:var(--ink)}
.hero-sub{left:0;width:1200px;top:524px;text-align:center;font-size:20px;color:var(--ink)}

/* nav */
.nav{left:0;top:668px;width:1200px;height:60px;background:#fff;box-shadow:0 -1px 0 #ddd}
.nav ul{list-style:none;position:absolute;left:162px;top:24px;display:flex;font-size:11px;font-weight:700;color:#333;letter-spacing:.5px}
.nav li{padding:0 36px;border-left:1px solid #999;line-height:12px;white-space:nowrap}
.nav li:first-child{border-left:0;padding-left:0;color:var(--red);position:relative}
.nav li:first-child::before{content:"";position:absolute;left:0;top:-27px;width:34px;height:4px;background:var(--red)}

/* intro */
.eyebrow{left:162px;top:790px;font-size:10px;color:var(--red)}
.intro-title{left:162px;top:812px;width:420px;font-size:36px;line-height:46px;color:var(--ink);white-space:nowrap}
.intro-title b{color:var(--red);font-weight:400}
.btn-outline{left:162px;top:938px;width:167px;height:40px;border:2px solid var(--red);color:var(--red);font-size:11px;font-weight:700;display:flex;align-items:center;justify-content:center;letter-spacing:.5px}
.intro-col{left:601px;top:796px;width:445px;font-size:11px;line-height:21px}
.intro-col h4{color:var(--red);font-size:10.5px;font-weight:700;margin-bottom:2px}
.intro-col p{margin-bottom:12px}

/* services */
.cell{width:300px;height:169px;border:1px solid var(--line);margin:-1px 0 0 -1px;text-align:center}
.cell.text{padding-top:40px;background:#fff}
.cell h5{font-size:10.5px;font-weight:700;color:#222;letter-spacing:.4px;margin-bottom:10px}
.cell p{font-size:11px;line-height:20px;width:230px;margin:0 auto}
.cell a{display:block;margin-top:10px;font-size:9.5px;color:var(--red);text-decoration:none}
.cell.icon{display:flex;align-items:center;justify-content:center}
.cell.icon svg{width:72px;height:72px}

/* why */
.why-title{left:0;width:1200px;top:1850px;text-align:center;font-size:40px;color:var(--ink)}
.why-title b{color:var(--red);font-weight:400}
.why-sub{left:0;width:1200px;top:1918px;text-align:center;font-size:12px}
.photo{position:absolute}
.photo .cap{position:absolute;left:22px;bottom:22px;color:#fff;font-weight:700;font-size:17px;letter-spacing:.5px;line-height:22px}
.photo .cap::before{content:"";display:block;width:34px;height:4px;background:#fff;margin-bottom:10px}

/* form */
.field{top:2606px;height:40px;border:1px solid #ddd;font-size:10px;color:#999;padding:12px 14px}
.send{left:953px;top:2606px;width:86px;height:40px;border:2px solid var(--red);color:var(--red);font-size:11px;font-weight:700;display:flex;align-items:center;justify-content:center}
.rule{left:0;top:2669px;width:1200px;height:1px;background:var(--line)}

/* footer */
.foot-mark{left:266px;top:2735px;width:56px;height:56px;border:5px solid var(--ink)}
.foot-name{left:162px;width:270px;text-align:center;color:var(--ink);font-weight:600;white-space:nowrap}
.badge{top:2735px;height:67px;background:var(--red);color:#fff;display:flex;align-items:center;gap:12px;padding-left:16px;font-size:10.5px;font-weight:700;line-height:13px}
.badge i{width:40px;height:30px;border:2px solid #fff;border-radius:6px;flex:none}
.foot-h{top:2846px;font-size:13px;font-weight:700;color:#222;letter-spacing:.5px}
.foot-h::after{content:"";display:block;width:26px;height:3px;background:var(--red);margin-top:8px}
.foot-links{left:458px;top:2892px;list-style:none;font-size:11px;line-height:26px}
.contact{left:686px;top:2880px;font-size:11px;line-height:18px}
.bottom{left:0;top:3068px;width:1200px;height:52px;background:var(--dark);color:#ddd;font-size:10px;padding:20px 162px}
.bottom-social{right:162px;top:3078px;display:flex;gap:8px}
.bottom-social span{width:28px;height:28px;border:1.5px solid #fff;border-radius:50%}
</style>
</head>
<body>

<!-- hero -->
<div class="abs hero" role="img" aria-label="Faded photo of rooftop aerials and satellite masts against a pale sky"></div>
<div class="abs social-top"><span></span><span></span><span></span></div>
<div class="abs phone-btn">
  <svg width="14" height="12" viewBox="0 0 14 12"><path d="M1 4c0-2 2-3 6-3s6 1 6 3v1h-3V3.5H4V5H1z M3 6h8l1 5H2z" fill="#fff"/></svg>
  012 555 0189
</div>
<div class="abs brand-mark"></div>
<div class="abs brand-name brand-1">KESTREL REACH</div>
<div class="abs brand-name brand-2">&amp; MEND</div>
<h1 class="abs hero-title serif">Kestrel Reach &amp; Mend</h1>
<p class="abs hero-sub serif">Same Day Smart Home TV Aerial &amp; Satellite Installations</p>

<nav class="abs nav">
  <ul>
    <li>HOME</li>
    <li>TV AERIAL SERVICES</li>
    <li>ORBIT SATELLITE TV</li>
    <li>SMART HOME</li>
    <li>CCTV &amp; ALARM</li>
    <li>WIFI HOME</li>
  </ul>
</nav>

<!-- intro -->
<div class="abs eyebrow">KESTREL REACH &amp; MEND</div>
<h2 class="abs intro-title serif">Smart Home TV Aerial<br>&amp; Satellite Installers<b>.</b></h2>
<div class="abs btn-outline">MORE ABOUT US</div>
<div class="abs intro-col">
  <h4>CONSECTETOR ADIPISCING</h4>
  <p>Lorem ipsum dolor sit amet, consectetur adipiscing elit, sed do eiusmod tempor incididunt ut labore et dolore magna aliqua. Ut enim ad minim veniam, quis nostrud exercitation ullamco laboris nisi ut aliquip ex ea commodo consequat. Duis aute</p>
  <h4>LOREM IPSUM DOLOR SIT AMET</h4>
  <p>Lorem ipsum dolor sit amet, consectetur adipiscing elit, sed do eiusmod tempor incididunt ut labore et dolore magna aliqua. Ut enim ad minim veniam, quis nostrud exercitation ullamco laboris nisi ut aliquip ex ea commodo consequat. Duis</p>
</div>

<!-- services grid -->
<div class="abs" style="left:1px;top:1074px;width:1200px">
  <div class="abs cell text" style="left:0;top:0"><h5>TV AERIAL SERVICES</h5><p>Lorem ipsum dolor sit amet, consectetur adipiscing elit, sed do eiusmod tempor</p><a>LEARN MORE</a></div>
  <div class="abs cell icon" style="left:300px;top:0"><svg viewBox="0 0 72 72"><path d="M20 20 L48 48 A20 20 0 0 1 20 20z" fill="#111" transform="rotate(-10 36 36)"/><line x1="36" y1="34" x2="52" y2="20" stroke="#111" stroke-width="3"/><circle cx="53" cy="19" r="3" fill="#111"/><path d="M22 62 L30 44 L38 62z" fill="#111"/></svg></div>
  <div class="abs cell text" style="left:600px;top:0"><h5>SOUND &amp; VISION</h5><p>Lorem ipsum dolor sit amet, consectetur adipiscing elit, sed do eiusmod tempor</p><a>LEARN MORE</a></div>
  <div class="abs cell icon" style="left:900px;top:0"><svg viewBox="0 0 72 72" fill="none" stroke="#111" stroke-width="3.5"><path d="M10 34 L36 12 L62 34 V60 H10z"/><path d="M26 40a14 14 0 0 1 20 0M30 45a8 8 0 0 1 12 0"/><circle cx="36" cy="50" r="2" fill="#111"/></svg></div>

  <div class="abs cell icon" style="left:0;top:168px"><svg viewBox="0 0 72 72"><line x1="28" y1="14" x2="36" y2="24" stroke="#111" stroke-width="3"/><line x1="46" y1="12" x2="36" y2="24" stroke="#111" stroke-width="3"/><rect x="10" y="24" width="52" height="36" rx="5" fill="#111"/><rect x="16" y="30" width="32" height="24" rx="3" fill="#fff"/><circle cx="55" cy="36" r="2.5" fill="#fff"/><circle cx="55" cy="46" r="2.5" fill="#fff"/></svg></div>
  <div class="abs cell text" style="left:300px;top:168px"><h5>ORBIT SATELITE</h5><p>Lorem ipsum dolor sit amet, consectetur adipiscing elit, sed do eiusmod tempor</p><a>LEARN MORE</a></div>
  <div class="abs cell icon" style="left:600px;top:168px"><svg viewBox="0 0 72 72" fill="none" stroke="#111" stroke-width="3"><circle cx="22" cy="26" r="12"/><circle cx="22" cy="26" r="4" fill="#111"/><rect x="30" y="30" width="30" height="30"/><path d="M42 52V38l10-3v14"/><circle cx="40" cy="52" r="3" fill="#111"/><circle cx="50" cy="49" r="3" fill="#111"/></svg></div>
  <div class="abs cell text" style="left:900px;top:168px"><h5>SMART HOME SYSTEM</h5><p>Lorem ipsum dolor sit amet, consectetur adipiscing elit, sed do eiusmod tempor</p><a>LEARN MORE</a></div>

  <div class="abs cell icon" style="left:300px;top:336px"><svg viewBox="0 0 72 72" fill="none" stroke="#111" stroke-width="4.5" stroke-linecap="round"><path d="M12 30a34 34 0 0 1 48 0M20 39a22 22 0 0 1 32 0M28 47a10 10 0 0 1 16 0"/><circle cx="36" cy="55" r="3" fill="#111"/></svg></div>
  <div class="abs cell text" style="left:600px;top:336px"><h5>COMMUNAL TV SYSTEM</h5><p>Lorem ipsum dolor sit amet, consectetur adipiscing elit, sed do eiusmod tempor</p><a>LEARN MORE</a></div>

  <div class="abs cell text" style="left:300px;top:504px"><h5>WI-FI SOLUTION</h5><p>Lorem ipsum dolor sit amet, consectetur adipiscing elit, sed do eiusmod tempor</p><a>LEARN MORE</a></div>
  <div class="abs cell icon" style="left:600px;top:504px"><svg viewBox="0 0 72 72"><path d="M24 20a18 18 0 0 1 24 0M29 26a10 10 0 0 1 14 0" fill="none" stroke="#111" stroke-width="3.5" stroke-linecap="round"/><circle cx="36" cy="31" r="2.5" fill="#111"/><path d="M16 48 L36 34 L56 48 H50 V62 H22 V48z" fill="#111"/><rect x="32" y="52" width="8" height="10" fill="#fff"/></svg></div>
</div>

<!-- why -->
<h2 class="abs why-title serif">Why Use Kestrel Reach &amp; Mend<b>.</b></h2>
<p class="abs why-sub">Lorem ipsum dolor sit amet, consectetur adipiscing elit, sed do eiusmod tempor incididunt ut labore et dolore magna aliqua.</p>

<div class="photo" style="left:0;top:1978px;width:566px;height:304px;background:linear-gradient(135deg,#2f3d4e,#5a6b7a 60%,#3b4a3a)" role="img" aria-label="Engineer in a hard hat on a phone call">
  <div class="cap">SAME DAY TV AERIAL INSTALLATIONS</div></div>
<div class="photo" style="left:566px;top:1978px;width:324px;height:304px;background:linear-gradient(160deg,#3a3c3e,#7a6a5e 55%,#2d2f31)" role="img" aria-label="Engineer working on aerial cabling">
  <div class="cap">LOCAL FRIENDLY &amp; QUALIFIED<br>ENGINEERS</div></div>
<div class="photo" style="left:890px;top:1978px;width:310px;height:304px;background:linear-gradient(160deg,#8c8c86,#5c5f5e 60%,#3e3f3c)" role="img" aria-label="Satellite dishes on a rooftop">
  <div class="cap">FREE NO OBLIGATION<br>ESTIMATES</div></div>
<div class="photo" style="left:0;top:2282px;width:320px;height:302px;background:linear-gradient(150deg,#a4a9ab,#6f7578 55%,#8e5a48)" role="img" aria-label="Satellite dish mounted on a brick wall"></div>
<div class="photo" style="left:320px;top:2282px;width:312px;height:302px;background:linear-gradient(180deg,#6fa3d0,#9cc2e0 55%,#6b4a3a)" role="img" aria-label="Satellite dish on a house roof under blue sky"></div>
<div class="photo" style="left:632px;top:2282px;width:568px;height:302px;background:linear-gradient(180deg,#b99a78,#d8b48a 45%,#8a4e34)" role="img" aria-label="Aerial masts on a brick chimney at sunset"></div>

<!-- contact form -->
<div class="abs field" style="left:162px;width:254px">Name</div>
<div class="abs field" style="left:426px;width:254px">Email</div>
<div class="abs field" style="left:689px;width:254px">Message</div>
<div class="abs send">SEND</div>
<div class="abs rule"></div>

<!-- footer -->
<div class="abs foot-mark"></div>
<div class="abs foot-name" style="top:2822px;font-size:14px;letter-spacing:8px">KESTREL REACH</div>
<div class="abs foot-name" style="top:2848px;font-size:12px;letter-spacing:8px">&amp; MEND</div>

<div class="abs badge" style="left:458px;width:187px"><i></i><span>SAME DAY<br>TV AERIAL<br>INSTALLATION</span></div>
<div class="abs badge" style="left:666px;width:181px"><i style="border-radius:50%;width:34px;height:34px"></i><span>5 YEAR<br>INSTALLATION<br>WARRANTY</span></div>
<div class="abs badge" style="left:863px;width:176px"><i style="width:30px;height:36px;border-radius:3px"></i><span>FREE NO<br>OBLIGATION<br>ESTIMATES</span></div>

<div class="abs foot-h" style="left:458px">NAVIGATIONS</div>
<ul class="abs foot-links">
  <li>Home</li><li>Our Story</li><li>OurPeople</li><li>Our Products &amp; Services</li><li>Contact Us</li>
</ul>
<div class="abs foot-h" style="left:686px">CONTACT</div>
<div class="abs contact">
  Lorem Ipsum Dolor Sit Amet<br>Consectetur Lorem Dolor Sit Amet Consect<br><br>
  Phone: (001) 555-0147<br><br>
  Email: info@kestrelreachmend.com
</div>

<div class="abs bottom">© Copyright 2018 Kestrel Reach &amp; Mend, All Rights Reserved.</div>
<div class="abs bottom-social"><span></span><span></span><span></span></div>

</body>
</html>
```